Ardenwell Building and Property Services needs a business card design

We need a business card design for our building and property services business. We already have a logo we just need a creative design and layout on a business card. Emphasis on clean, modern, professional.
Our client targets are mainly body corporates, building managers, construction managers.
We are a building services company that lean more to structural repair of buildings, through concrete rectification and carbon fibre strengthening.
We also refurbish facades, rendering, painting etc
We target higher end body corporates in prestigious locations, hence why we'd like our cards to reflect professionalism, strength, efficiency

Target Market(s)

body corporates, building managers, construction managers

Industry/Entity Type

Construction

Contact Information for Business Card

Ardenwell is the main word, with 'Building and Property Services' underneath.
Level 17, 82 Harlow Street
MERRIDALE
Melbourne
Vic 3094
T: 9518 2736
Duncan Ferris - Director
dunardenwell@mailbox-example.com

Requirements
Must have
• Stand out on the back of the card- strong/ bold, company logo
• All of the contact details written above
Should not have
• I'd like the card to stand out, especially on the back. Id like the company logo to be prominent, although feel free to be creative around it. But remain clean and professional

```html
<!DOCTYPE html>
<html lang="en">
<head>
<meta charset="utf-8">
<title>Ardenwell Building and Property Services – Business Card</title>
<link rel="stylesheet" href="https://fonts.googleapis.com/css2?family=Lora:wght@400;700&display=swap">
<style>
  :root {
    --backdrop: #3d3d3d;
    --card-white: #ffffff;
    --card-black: #1f1f1f;
    --band-black: #1a1a1a;
    --brand-blue: #2a8fd4;
    --ink: #222222;
    --ink-soft: #666666;
    --ink-light: #d8d8d8;
    --rule: #d4d4d4;
  }
  * { box-sizing: border-box; margin: 0; padding: 0; }
  html, body { width: 1200px; height: 800px; overflow: hidden; }
  body {
    background: var(--backdrop);
    display: flex;
    align-items: center;
    justify-content: center;
    gap: 60px;
    font-family: "Lora", Georgia, serif;
  }
  .card {
    position: relative;
    width: 520px;
    height: 300px;
    border-radius: 3px;
    overflow: hidden;
    box-shadow: 0 10px 28px rgba(0,0,0,0.45);
  }
  .card-front { background: var(--card-white); }
  .card-back {
    background: var(--card-black);
    display: flex;
    align-items: center;
    justify-content: center;
  }

  .brand {
    display: grid;
    grid-template-columns: auto auto;
    column-gap: 12px;
    align-items: center;
    font-family: "Lora", Georgia, serif;
  }
  .brand-mark {
    grid-row: 1 / span 2;
    width: 30px;
    height: 30px;
    border-radius: 50%;
    background: var(--brand-blue);
  }
  .brand-name {
    font-weight: 400;
    font-size: 26px;
    line-height: 1.1;
    color: var(--brand-blue);
  }
  .brand-tagline {
    font-weight: 400;
    font-size: 9px;
    color: var(--ink-soft);
    margin-top: 2px;
  }

  .card-front .brand {
    position: absolute;
    left: 30px;
    top: 104px;
  }

  .card-back .brand { column-gap: 18px; }
  .card-back .brand-mark { width: 52px; height: 52px; }
  .card-back .brand-name { font-size: 44px; }
  .card-back .brand-tagline { font-size: 13px; color: var(--ink-light); margin-top: 4px; }

  .divider {
    position: absolute;
    left: 258px;
    top: 58px;
    width: 1px;
    height: 140px;
    background: var(--rule);
  }

  .contact {
    position: absolute;
    left: 276px;
    top: 40px;
    color: var(--ink-soft);
    font-size: 11.5px;
    line-height: 1.45;
  }
  .contact-name {
    color: var(--ink);
    font-size: 21px;
    font-weight: 400;
    line-height: 1.15;
  }
  .contact-role {
    color: var(--ink);
    font-size: 11.5px;
    font-weight: 700;
    margin-bottom: 10px;
  }
  .contact-block { margin-bottom: 8px; }

  .base-band {
    position: absolute;
    left: 0;
    bottom: 0;
    width: 520px;
    height: 80px;
  }
  .band-black { fill: var(--band-black); }
  .band-blue { fill: var(--brand-blue); }
</style>
</head>
<body>
  <section class="card card-front" aria-label="Business card front">
    <div class="brand">
      <div class="brand-mark"></div>
      <div class="brand-name">Ardenwell</div>
      <div class="brand-tagline">Building and Property Services</div>
    </div>

    <div class="divider"></div>

    <div class="contact">
      <div class="contact-name">Duncan Ferris</div>
      <div class="contact-role">Director</div>
      <div class="contact-block">
        <div>95 18 27 36</div>
        <div>dunardenwell@mailbox-example.com</div>
      </div>
      <div class="contact-block">
        <div>Level 17, 82 Harlow Street</div>
        <div>MERRIDALE</div>
        <div>Melbourne Vic 3094</div>
      </div>
    </div>

    <svg class="base-band" viewBox="0 0 520 80" aria-hidden="true">
      <polygon class="band-blue" points="476,8 520,8 520,30 470,30"/>
      <polygon class="band-black" points="250,30 520,30 520,80 0,80 0,52 244,52"/>
      <polygon class="band-blue" points="0,64 236,64 232,80 0,80"/>
    </svg>
  </section>

  <section class="card card-back" aria-label="Business card back">
    <div class="brand">
      <div class="brand-mark"></div>
      <div class="brand-name">Ardenwell</div>
      <div class="brand-tagline">Building and Property Services</div>
    </div>
  </section>
</body>
</html>
```